Bref créative
Trucking Company Business Cards Stationary
KVR Freight Solutions
Professional
Beto Quiroga
Terminal Manager
4100 Harborview Blvd
La Porte, TX 77571
kvrfreightsolutions@mailbox-example.com
i would like something similar to this on the back side of card
i would also like something similar to this on the back side of my card

```html
<!DOCTYPE html>
<html lang="en">
<head>
<meta charset="utf-8">
<title>KVR Freight Solutions — Stationery</title>
<link href="https://fonts.googleapis.com/css2?family=Arimo:wght@400;700&display=swap" rel="stylesheet">
<style>
  :root {
    --red: #c8141e;
    --red-dark: #9d0e16;
    --grey: #a9abae;
    --ink: #3a3a3a;
    --paper: #ffffff;
    --stage: #eceeef;
  }
  * { box-sizing: border-box; margin: 0; padding: 0; }
  html, body { width: 1200px; height: 936px; overflow: hidden; }
  body { background: var(--stage); font-family: "Arimo", Arial, sans-serif; color: var(--ink); position: relative; }

  .sheet { position: absolute; background: var(--paper); overflow: hidden; }
  .band { position: absolute; left: 0; bottom: 0; width: 100%; display: block; }
  .band-url { position: absolute; left: 0; right: 0; text-align: center; color: #fff; font-weight: 700; letter-spacing: 0.5px; }

  .brand-name { color: var(--red); font-weight: 700; white-space: nowrap; }

  /* Letterhead */
  .letterhead { left: 177px; top: 63px; width: 393px; height: 552px; }
  .letterhead .brand-name { position: absolute; left: 30px; top: 40px; font-size: 17px; }
  .letterhead .contact { position: absolute; right: 22px; top: 24px; font-size: 6px; line-height: 9px; color: #666; }
  .letter { position: absolute; left: 30px; top: 112px; width: 300px; font-size: 5.5px; line-height: 8.5px; color: #555; }
  .letter p { margin-bottom: 10px; }
  .letter .sign-space { height: 22px; }
  .letterhead .band-url { bottom: 10px; font-size: 11px; }

  /* Cover sheet */
  .cover { left: 638px; top: 63px; width: 387px; height: 552px; }
  .cover .brand-name { position: absolute; left: 0; right: 0; top: 185px; text-align: center; font-size: 30px; }
  .cover .band-url { bottom: 10px; font-size: 11px; }

  /* Business cards */
  .card { width: 189px; height: 107px; }
  .card-info { left: 56px; top: 653px; }
  .card-logo { left: 56px; top: 772px; }
  .card-info .brand-name { position: absolute; left: 10px; top: 10px; font-size: 10px; }
  .card-info .details { position: absolute; left: 10px; top: 34px; font-size: 5px; line-height: 7.5px; color: #555; }
  .card-info .details .person { font-size: 6px; font-weight: 700; color: var(--ink); }
  .card-logo .brand-name { position: absolute; left: 0; right: 0; top: 30px; text-align: center; font-size: 11px; }
  .card-logo .band-url { bottom: 4px; font-size: 6px; }

  /* Envelopes */
  .envelope-front { left: 286px; top: 648px; width: 410px; height: 238px; }
  .envelope-front .brand-name { position: absolute; left: 16px; top: 14px; font-size: 10px; }
  .envelope-front .return { position: absolute; left: 16px; top: 30px; font-size: 5px; line-height: 7px; color: #666; }
  .envelope-back { left: 736px; top: 648px; width: 423px; height: 238px; }
  .envelope-back .flap { position: absolute; left: 0; top: 0; width: 100%; height: 100%; }
  .envelope-back .band-url { top: 52px; font-size: 12px; }
</style>
</head>
<body>

  <!-- Letterhead -->
  <section class="sheet letterhead">
    <div class="brand-name">KVR Freight Solutions</div>
    <div class="contact">
      4100 Harborview Blvd<br>
      La Porte, TX 77571<br>
      Beto Quiroga<br>
      kvrfreightsolutions@mailbox-example.com
    </div>
    <div class="letter">
      <p>July 1, 2014</p>
      <p>Dear Sir,</p>
      <p>Thank you for considering our freight services. We move loads across Texas and beyond with care, clear pricing and drivers who know the road. Our team keeps every shipment on schedule and every customer informed.</p>
      <p>We would welcome the chance to quote your next route. Please reach out with lane details and volumes, and we will reply within one business day.</p>
      <p>Thank you for your time and trust.</p>
      <p>Best Regards,</p>
      <div class="sign-space"></div>
      <p>Beto Quiroga<br>Terminal Manager<br>4100 Harborview Blvd, La Porte, TX 77571</p>
    </div>
    <svg class="band" viewBox="0 0 393 70" height="70" preserveAspectRatio="none" aria-hidden="true">
      <path d="M0 26 Q200 -6 393 14 L393 22 Q200 4 0 34 Z" fill="var(--grey)"/>
      <path d="M0 34 Q200 4 393 22 L393 70 L0 70 Z" fill="var(--red)"/>
    </svg>
    <div class="band-url">www.kvrfreight-example.com</div>
  </section>

  <!-- Cover sheet -->
  <section class="sheet cover">
    <div class="brand-name">KVR Freight Solutions</div>
    <svg class="band" viewBox="0 0 387 70" height="70" preserveAspectRatio="none" aria-hidden="true">
      <path d="M0 26 Q200 -6 387 14 L387 22 Q200 4 0 34 Z" fill="var(--grey)"/>
      <path d="M0 34 Q200 4 387 22 L387 70 L0 70 Z" fill="var(--red)"/>
    </svg>
    <div class="band-url">www.kvrfreight-example.com</div>
  </section>

  <!-- Business card: contact side -->
  <section class="sheet card card-info">
    <div class="brand-name">KVR Freight Solutions</div>
    <div class="details">
      <span class="person">Beto Quiroga</span><br>
      Terminal Manager<br>
      4100 Harborview Blvd<br>
      La Porte, TX 77571<br>
      kvrfreightsolutions@mailbox-example.com
    </div>
    <svg class="band" viewBox="0 0 189 18" height="18" preserveAspectRatio="none" aria-hidden="true">
      <path d="M0 6 Q100 -2 189 4 L189 7 Q100 2 0 9 Z" fill="var(--grey)"/>
      <path d="M0 9 Q100 2 189 7 L189 18 L0 18 Z" fill="var(--red)"/>
    </svg>
  </section>

  <!-- Business card: brand side -->
  <section class="sheet card card-logo">
    <div class="brand-name">KVR Freight Solutions</div>
    <svg class="band" viewBox="0 0 189 24" height="24" preserveAspectRatio="none" aria-hidden="true">
      <path d="M0 8 Q100 -2 189 5 L189 9 Q100 3 0 12 Z" fill="var(--grey)"/>
      <path d="M0 12 Q100 3 189 9 L189 24 L0 24 Z" fill="var(--red)"/>
    </svg>
    <div class="band-url">www.kvrfreight-example.com</div>
  </section>

  <!-- Envelope front -->
  <section class="sheet envelope-front">
    <div class="brand-name">KVR Freight Solutions</div>
    <div class="return">
      4100 Harborview Blvd<br>
      La Porte, TX 77571
    </div>
  </section>

  <!-- Envelope back -->
  <section class="sheet envelope-back">
    <svg class="flap" viewBox="0 0 423 238" preserveAspectRatio="none" aria-hidden="true">
      <polygon points="0,0 423,0 423,70 212,128 0,70" fill="var(--red)"/>
      <polygon points="0,70 212,128 423,70 423,74 212,132 0,74" fill="var(--red-dark)" opacity="0.5"/>
    </svg>
    <div class="band-url">www.kvrfreight-example.com</div>
  </section>

</body>
</html>
```